Varnel Group Limited Stationary

We are in need of business card and letterhead designs. We are looking for clean modern designs that complement the style and feel of our logo.

Industry/Entity Type

Business

```html
<!DOCTYPE html>
<html lang="en">
<head>
<meta charset="utf-8">
<title>Varnel Group – Business Cards</title>
<link href="https://fonts.googleapis.com/css2?family=EB+Garamond:wght@400;500&display=swap" rel="stylesheet">
<style>
  :root {
    --brand-blue: #0b3d82;
    --card-white: #ececec;
    --ink: #3a3a3a;
    --muted: #5a5a5a;
    --backdrop: #d9d6d1;
    --white: #ffffff;
  }
  * { box-sizing: border-box; margin: 0; padding: 0; }
  html, body {
    width: 1200px; height: 900px; overflow: hidden;
    background: var(--backdrop);
    font-family: "EB Garamond", Georgia, serif;
  }
  .stage {
    position: relative; width: 1200px; height: 900px;
  }
  .card {
    position: absolute; top: 307px;
    width: 500px; height: 286px;
    box-shadow: 0 6px 18px rgba(0,0,0,0.18);
  }
  /* Back of card */
  .card-back {
    left: 70px; background: var(--brand-blue); color: var(--white);
  }
  .card-back .mark {
    position: absolute; left: 50%; top: 62px; transform: translateX(-50%);
    display: flex; flex-direction: column; align-items: center; gap: 12px;
  }
  .card-back .mark-circle {
    width: 74px; height: 74px; border-radius: 50%; background: var(--card-white);
  }
  .card-back .mark-name {
    font-size: 26px; font-weight: 400; letter-spacing: 3px; text-transform: uppercase;
    color: var(--white);
  }
  .card-back .web {
    position: absolute; right: 36px; bottom: 30px;
    font-size: 13px; letter-spacing: 0.5px; color: var(--white);
  }
  /* Front of card */
  .card-front {
    left: 630px; background: var(--card-white); color: var(--ink);
  }
  .card-front .identity {
    position: absolute; left: 30px; bottom: 70px;
    display: flex; flex-direction: column; align-items: flex-start; gap: 10px;
  }
  .card-front .identity-circle {
    width: 52px; height: 52px; border-radius: 50%; background: var(--brand-blue);
    margin-left: 34px;
  }
  .card-front .identity-name {
    font-size: 27px; font-weight: 400; letter-spacing: 2px; text-transform: uppercase;
    color: var(--brand-blue); line-height: 1;
  }
  .card-front .identity-rule {
    width: 190px; height: 1px; background: var(--brand-blue); opacity: 0.6;
  }
  .card-front .contact {
    position: absolute; left: 280px; top: 34px; width: 200px;
  }
  .contact .person-name { font-size: 20px; font-weight: 500; color: var(--ink); line-height: 1.1; }
  .contact .person-role {
    font-size: 11px; letter-spacing: 1.5px; text-transform: uppercase; color: var(--muted);
    margin-top: 2px;
  }
  .contact .lines { margin-top: 14px; font-size: 12.5px; line-height: 1.35; color: var(--muted); }
  .contact .lines dt {
    float: left; clear: left; width: 14px; font-weight: 500; color: var(--brand-blue);
  }
  .contact .lines dd { margin-left: 16px; }
  .contact .address { margin-top: 14px; font-size: 12.5px; line-height: 1.35; color: var(--muted); font-style: normal; }
  .card-front .band {
    position: absolute; left: 0; right: 0; bottom: 14px; height: 22px;
    background: var(--brand-blue);
  }
</style>
</head>
<body>
  <main class="stage">
    <section class="card card-back" aria-label="Business card back">
      <div class="mark">
        <span class="mark-circle"></span>
        <span class="mark-name">Varnel Group</span>
      </div>
      <p class="web">www.varnelgroup.com</p>
    </section>

    <section class="card card-front" aria-label="Business card front">
      <div class="identity">
        <span class="identity-circle"></span>
        <span class="identity-name">Varnel Group</span>
        <span class="identity-rule"></span>
      </div>
      <div class="contact">
        <p class="person-name">Marion Keller</p>
        <p class="person-role">Manager</p>
        <dl class="lines">
          <dt>T</dt><dd>(312) 47 208 61 30</dd>
          <dt>M</dt><dd>(312) 66 174 38 92</dd>
          <dt>E</dt><dd>keller@varnelgroup.com</dd>
        </dl>
        <address class="address">418 W. Harmon St, #902<br>Springdale, IL 60412</address>
      </div>
      <div class="band"></div>
    </section>
  </main>
</body>
</html>
```